"Kestrelmoor Accupuncture" needs a Promotional Card - A6 size

Requirements
Must have
• Bright colours, pictures of happy people, acupuncture-related pictures.

```html
<!DOCTYPE html>
<html lang="en">
<head>
<meta charset="utf-8">
<title>Kestrelmoor Accupuncture – Promotional Cards</title>
<link rel="stylesheet" href="https://fonts.googleapis.com/css2?family=Arimo:wght@400;700&display=swap">
<style>
  :root {
    --orange: #f5862a;
    --brand-red: #e2462a;
    --page: #ecebe8;
    --white: #ffffff;
    --slate-band: rgba(140, 150, 163, 0.72);
    --grey-text: #8a8f96;
    --body-font: "Arimo", Arial, sans-serif;
  }
  * { box-sizing: border-box; margin: 0; padding: 0; }
  html, body { width: 1200px; height: 1000px; overflow: hidden; }
  body { background: var(--page); font-family: var(--body-font); position: relative; }

  .card { position: absolute; overflow: hidden; box-shadow: 0 3px 8px rgba(0,0,0,0.22); }
  .photo { position: absolute; }
  .quote-mark { color: var(--orange); font-weight: 700; line-height: 1; position: absolute; font-family: Georgia, "Times New Roman", serif; }
  .quote-text { color: var(--white); font-weight: 700; position: absolute; line-height: 1.3; white-space: nowrap; letter-spacing: -0.3px; }

  /* ---------- Landscape card ---------- */
  .card--landscape { left: 75px; top: 30px; width: 773px; height: 542px; background: var(--white); }
  .card--landscape .photo--hero {
    left: 0; top: 0; width: 773px; height: 542px;
    background:
      radial-gradient(ellipse 170px 150px at 560px 200px, #d9b9a0 0%, rgba(217,185,160,0.55) 45%, rgba(217,185,160,0) 100%),
      radial-gradient(ellipse 260px 120px at 650px 370px, #ece8e4 0%, rgba(236,232,228,0) 100%),
      radial-gradient(ellipse 300px 90px at 260px 330px, #c7a994 0%, rgba(199,169,148,0.4) 50%, rgba(199,169,148,0) 100%),
      linear-gradient(180deg, #e7ecf3 0%, #dfe5ee 55%, #eef0f3 100%);
  }
  .card--landscape .headline-band { position: absolute; left: 0; top: 30px; width: 773px; height: 98px; background: var(--slate-band); }
  .card--landscape .quote-mark { font-size: 88px; }
  .card--landscape .quote-text { font-size: 26px; }

  .relief-box {
    position: absolute; left: 0; top: 273px; width: 135px; height: 117px;
    background: var(--orange); color: var(--white);
    padding: 11px 0 0 46px; font-size: 14px; line-height: 19px;
  }
  .relief-box .relief-title { font-weight: 700; font-size: 15px; margin-bottom: 2px; }

  .contact-strip { position: absolute; left: 0; top: 400px; width: 773px; height: 142px; background: rgba(255,255,255,0.9); }
  .call-label { position: absolute; left: 46px; top: 51px; color: var(--grey-text); font-size: 14px; line-height: 17px; }
  .phone { position: absolute; left: 118px; top: 30px; color: var(--orange); font-size: 70px; font-weight: 700; letter-spacing: -1.5px; line-height: 1.15; }
  .brand { position: absolute; color: var(--brand-red); font-weight: 700; text-align: center; }
  .brand-dot { display: block; width: 14px; height: 14px; border-radius: 50%; background: var(--orange); margin: 0 auto 6px; }
  .address { position: absolute; color: var(--grey-text); font-size: 15px; white-space: nowrap; }

  /* ---------- Square card ---------- */
  .card--square { left: 490px; top: 588px; width: 650px; height: 400px; background: linear-gradient(160deg, #a9c0d6 0%, #7f9dba 55%, #4c6885 100%); }
  .card--square .photo--portrait {
    left: 0; top: 0; width: 650px; height: 400px;
    background:
      radial-gradient(ellipse 190px 200px at 470px 250px, #e8b9a0 0%, #d99d80 45%, rgba(200,120,90,0) 100%),
      radial-gradient(ellipse 250px 230px at 420px 150px, #a9522e 0%, rgba(169,82,46,0.7) 50%, rgba(169,82,46,0) 100%),
      linear-gradient(90deg, rgba(127,157,186,0) 0%, rgba(127,157,186,0) 30%, rgba(180,130,110,0.35) 55%, rgba(150,170,190,0.5) 100%);
  }
  .card--square .quote-mark { font-size: 62px; }
  .card--square .quote-text { font-size: 19px; }

  .square-quote-top { position: absolute; left: 0; top: 22px; width: 210px; height: 66px; background: rgba(80, 104, 128, 0.55); }
  .brand-panel { position: absolute; right: 22px; top: 10px; width: 180px; height: 120px; background: rgba(255,255,255,0.38); }
  .relief-band {
    position: absolute; left: 0; top: 150px; width: 280px; height: 96px;
    background: rgba(70, 94, 118, 0.5); color: var(--white); font-size: 15px; line-height: 20px;
  }
  .relief-band .col { position: absolute; top: 14px; }
  .relief-band .col--left { left: 42px; }
  .relief-band .col--right { left: 166px; top: 12px; }
  .relief-band .relief-title { font-weight: 700; font-size: 13px; margin-bottom: 2px; }

  .specialist { position: absolute; left: 82px; top: 268px; width: 80px; color: #dfe6ed; font-size: 10px; line-height: 12px; }
  .specialist .photo--doctor {
    position: relative; width: 72px; height: 82px; border: 3px solid var(--white);
    background: linear-gradient(180deg, #dcd9d5 0%, #b89c8c 55%, #6d4a5e 100%); margin-bottom: 4px;
  }
  .square-quote-bottom { position: absolute; left: 170px; top: 268px; width: 285px; height: 76px; background: rgba(50, 70, 92, 0.72); }
</style>
</head>
<body>

  <section class="card card--landscape" aria-label="Landscape promotional card">
    <div class="photo photo--hero" role="img" aria-label="Photo of a happy smiling woman reaching out to hold hands, bright soft background"></div>

    <div class="headline-band">
      <span class="quote-mark" style="left:28px; top:-8px;">“</span>
      <p class="quote-text" style="left:88px; top:12px;">Improve your<br>well-being</p>
      <span class="quote-mark" style="left:236px; top:38px;">”</span>

      <span class="quote-mark" style="left:362px; top:-8px;">“</span>
      <p class="quote-text" style="left:420px; top:12px;">Improve your physical<br>&amp; emotional balance.</p>
      <span class="quote-mark" style="left:690px; top:40px;">”</span>
    </div>

    <div class="relief-box">
      <p class="relief-title">Relief For</p>
      <p>Back Pain</p>
      <p>Headaches</p>
      <p>Weight Loss</p>
      <p>Insomnia</p>
    </div>

    <div class="contact-strip">
      <p class="call-label">CALL US<br>TODAY</p>
      <p class="phone">123-456-7890</p>
      <p class="brand" style="left:586px; top:14px; font-size:17px; line-height:18px; width:150px;">
        <span class="brand-dot"></span>Kestrelmoor<br>Accupuncture
      </p>
      <p class="address" style="left:598px; top:82px;">123 Street Name</p>
    </div>
  </section>

  <section class="card card--square" aria-label="Square promotional card">
    <div class="photo photo--portrait" role="img" aria-label="Close-up photo of a laughing older woman with red hair"></div>

    <div class="brand-panel">
      <p class="brand" style="left:0; top:18px; width:180px; font-size:16px; line-height:17px;">
        <span class="brand-dot"></span>Kestrelmoor<br>Accupuncture
      </p>
      <p class="address" style="left:32px; top:88px; font-size:12px; color:#6e7680;">123 Street Name</p>
    </div>

    <div class="square-quote-top">
      <span class="quote-mark" style="left:10px; top:-4px;">“</span>
      <p class="quote-text" style="left:46px; top:9px;">Improve your<br>well-being</p>
      <span class="quote-mark" style="left:172px; top:22px;">”</span>
    </div>

    <div class="relief-band">
      <div class="col col--left">
        <p class="relief-title">Relief For</p>
        <p>Back Pain</p>
        <p>Headaches</p>
      </div>
      <div class="col col--right">
        <p>Weight Loss</p>
        <p>Insomnia</p>
      </div>
    </div>

    <div class="specialist">
      <div class="photo photo--doctor" role="img" aria-label="Portrait photo of the specialist"></div>
      <p>Dr Name here</p>
      <p>Specialist</p>
    </div>

    <div class="square-quote-bottom">
      <span class="quote-mark" style="left:6px; top:8px;">“</span>
      <p class="quote-text" style="left:42px; top:13px;">Improve your physical<br>&amp; emotional balance.</p>
      <span class="quote-mark" style="left:250px; top:28px;">”</span>
    </div>
  </section>

</body>
</html>
```